Kestrel Works Business Cards

This job is for the design of a business card.
I would like to review the design in 2x colour tones to choose from black and white inverted.
EG:
Black with white logo and white with black logo on BACK
White with black text on front and black with white text options
PRINTING DIMENSIONS: 4.5 x 8.5cm
Complete design will need to be provided in ready to print format with bleed lines
Target Market(s)
The audience of my business are people in the trade industry.
It will be also used for general networking with trades people and possible future clients.
I want to be represented as a professional, dynamic, creative and personable operator.
The card should reflect style, taste, experience, professionalism.
Industry/Entity Type
Business
Requirements
Must have
- BACK CONTENT:
- Logo in white and black background and vice versa with WHITE card and black logo review samples.
- FRONT CARD CONTENT:
- Name: Morgan Telvane
- Director
- Phone: 0438 216 947
- Email: morgan@kestrelworks.com.au
- Web: kestrelworks.com.au
- LICENCE #: KT-R 72158
Nice to have
- Possibly a textured background design on rear as a pose to a solid black
- Possibly adding a blue or orange discreet colour tone (possibly for email, phone abbreviated letter or symbols).

```html
<!DOCTYPE html>
<html lang="en">
<head>
<meta charset="utf-8">
<title>Kestrel Works Business Cards</title>
<link rel="stylesheet" href="https://fonts.googleapis.com/css2?family=Arimo:wght@400;700&display=swap">
<style>
  :root {
    --stage: #1c1c1e;
    --card-light: #eeeeec;
    --card-dark: #26272a;
    --ink-dark: #2a2a2a;
    --ink-light: #f2f2f2;
    --muted-dark: #555555;
    --muted-light: #c9c9c9;
    --accent: #3fae49;
    --rule-dark: #3c3d41;
  }
  * { margin: 0; padding: 0; box-sizing: border-box; }
  html, body {
    width: 1200px;
    height: 900px;
    overflow: hidden;
    background: var(--stage);
    font-family: "Arimo", Arial, sans-serif;
  }
  .stage {
    position: relative;
    width: 1200px;
    height: 900px;
  }
  .card {
    position: absolute;
    width: 612px;
    height: 324px;
    display: flex;
    flex-direction: column;
    align-items: center;
    box-shadow: 0 18px 40px rgba(0, 0, 0, 0.55);
  }
  .card--light {
    left: 140px;
    top: 110px;
    background: var(--card-light);
    color: var(--ink-dark);
  }
  .card--dark {
    left: 448px;
    top: 430px;
    background: var(--card-dark);
    color: var(--ink-light);
  }
  .wordmark {
    margin-top: 66px;
    display: flex;
    align-items: center;
    gap: 10px;
    font-size: 34px;
    font-weight: 400;
    letter-spacing: 1px;
    text-transform: uppercase;
  }
  .wordmark__square {
    width: 22px;
    height: 22px;
    background: currentColor;
  }
  .identity {
    margin-top: 70px;
    font-size: 14px;
  }
  .identity__name {
    font-weight: 700;
    letter-spacing: 0.5px;
  }
  .slash { color: var(--accent); font-weight: 700; }
  .card--dark .identity { margin-top: 62px; }
  .divider {
    width: 280px;
    height: 1px;
    margin-top: 12px;
    background: var(--rule-dark);
  }
  .contact {
    margin-top: 14px;
    font-size: 13px;
    white-space: nowrap;
  }
  .card--dark .contact { margin-top: 12px; }
  .licence {
    margin-top: 8px;
    font-size: 12px;
    white-space: nowrap;
  }
  .contact__label { color: var(--accent); font-weight: 700; }
  .card--light .contact__value { color: var(--ink-dark); }
  .card--dark .contact__value { color: var(--muted-light); }
  .sep { padding: 0 4px; }
</style>
</head>
<body>
<main class="stage">
  <section class="card card--light" aria-label="White card">
    <div class="wordmark"><span class="wordmark__square"></span>Kestrel Works</div>
    <p class="identity"><span class="identity__name">MORGAN TELVANE</span> <span class="slash">/</span> Director</p>
    <p class="contact">
      <span class="contact__label">T:</span> <span class="contact__value">0438216947</span><span class="sep">·</span><span class="contact__label">E:</span> <span class="contact__value">morgan@kestrelworks.com.au</span><span class="sep">·</span><span class="contact__value">www.kestrelworks.com.au</span>
    </p>
    <p class="licence"><span class="contact__label">LIC:</span> <span class="contact__value">KT-R 72158</span></p>
  </section>

  <section class="card card--dark" aria-label="Black card">
    <div class="wordmark"><span class="wordmark__square"></span>Kestrel Works</div>
    <p class="identity"><span class="identity__name">MORGAN TELVANE</span> <span class="slash">/</span> Director</p>
    <div class="divider"></div>
    <p class="contact">
      <span class="contact__label">T:</span> <span class="contact__value">0438216947</span><span class="sep">·</span><span class="contact__label">E:</span> <span class="contact__value">morgan@kestrelworks.com.au</span><span class="sep">·</span><span class="contact__value">www.kestrelworks.com.au</span>
    </p>
    <p class="licence"><span class="contact__label">LIC:</span> <span class="contact__value">KT-R 72158</span></p>
  </section>
</main>
</body>
</html>
```